Youth Sports Banner Ad - 3x5 ft banner special!

We are looking for a full page ad (8.5x11") to advertise our banner services for Youth Sports leagues. The flyers will be handed out to teams and parents in hopes to draw their business to us for team banners.
We want to show our logo, address (4816 Corliss Ln. Paso Robles). Please include that we are offering a youth sports special price on 3x5 ft team banners for $115 (plus tax). The pricing will include 1 layout with up to 2 revisions. We would like the ad to grab the attention of the audience and ask them to "Call, Email or Stop in Today!"

Our info that needs to be on the banner includes:
email: info@markwell202.example
phone: 805-219-6847

We want to really focus on our quick turnaround as we will be producing the banners withing 1-2 business days after artwork approval.
We would like to include the banner samples if possible, and if you see fit, also include that we would like the potential customer to email us their teams name, roster, and colors to help speed up the layout process.

Target Market(s)

Parents of kids playing youth sports. The flyer is meant to increase awareness of our sign shop, while offering a great discount on banners for youth sports banners.

Font styles to use
Sans Serif

Colors

Designer to choose colors to be used in the design.

Requirements
Must have
• Our logo, $115 plus tax banner price, our business information, request to send over all team information including name, roster, and team colors.
Nice to have
• Would like to see color in the ad! If you can tie in the Kelly green from our logo, that would be great.

```html
<!DOCTYPE html>
<html lang="en">
<head>
<meta charset="utf-8">
<title>Markwell – Youth Sports Banner Special</title>
<link rel="stylesheet" href="https://fonts.googleapis.com/css2?family=Oswald:wght@700&family=Bebas+Neue&family=Open+Sans:wght@400;700&display=swap">
<style>
  :root{
    --kelly:#1fb537;
    --kelly-bright:#22c33b;
    --kelly-deep:#0f8a25;
    --ink:#0b0b0b;
    --paper:#ffffff;
    --price:#f4ec1c;
    --tag:#e3195a;
    --stage:#dcd9d4;
  }
  *{box-sizing:border-box;margin:0;padding:0}
  html,body{width:1200px;height:1135px;overflow:hidden;background:var(--stage)}
  .flyer{
    position:absolute;left:215px;top:22px;width:770px;height:1090px;
    background:linear-gradient(180deg,var(--paper) 0%,var(--paper) 30%,#eceeef 60%,#cfd2d4 80%);
    overflow:hidden;box-shadow:0 4px 18px rgba(0,0,0,.25);
    font-family:"Open Sans",sans-serif;
  }
  .flyer-shapes{position:absolute;inset:0}
  .brand{
    position:absolute;left:40px;top:112px;width:270px;
    display:flex;align-items:center;gap:12px;
  }
  .brand-mark{flex:none;width:20px;height:20px;background:var(--kelly)}
  .brand-name{
    font-family:"Oswald",sans-serif;font-weight:700;font-size:46px;line-height:1;
    color:var(--kelly);letter-spacing:1px;white-space:nowrap;
  }
  .cta{position:absolute;left:328px;width:442px;background:var(--ink);
    font-family:"Bebas Neue",sans-serif;color:var(--kelly-bright);font-size:58px;
    line-height:1;padding-left:20px;display:flex;align-items:center}
  .cta-top{top:52px;height:71px}
  .cta-bottom{top:142px;height:85px}
  .offer{
    position:absolute;left:95px;top:352px;width:560px;
    transform:rotate(-10deg);transform-origin:center;text-align:center;
  }
  .offer-headline{
    font-family:"Bebas Neue",sans-serif;font-weight:400;font-size:46px;line-height:44px;color:#fff;
    letter-spacing:.5px;
  }
  .offer-headline .hl{color:var(--price)}
  .offer-note{margin-top:20px;font-size:27px;line-height:32px;color:#fff}
  .sample{position:absolute;transform:rotate(5deg)}
  .sample-art{width:100%;height:100%;box-shadow:0 6px 12px rgba(0,0,0,.35)}
  .sample-tag{
    position:absolute;left:4px;top:-16px;background:var(--tag);color:#fff;
    font-weight:700;font-size:12px;padding:1px 10px 3px;border-radius:3px 3px 0 0;
  }
  .sample-soccer{left:70px;top:665px;width:310px;height:180px}
  .sample-soccer .sample-art{background:radial-gradient(circle at 45% 50%,#3d3db4,#1c1c78 70%)}
  .sample-baseball{left:392px;top:660px;width:338px;height:195px}
  .sample-baseball .sample-art{background:linear-gradient(90deg,#111 0%,#1a1a1a 60%,#2a1a08 100%);border-bottom:14px solid #f28a1a}
  .turnaround{
    position:absolute;left:0;top:891px;width:770px;height:80px;
    display:flex;align-items:center;justify-content:center;text-align:center;
    color:#fff;font-weight:700;font-size:14.5px;line-height:20px;padding:0 40px;
  }
  .contact{position:absolute;left:40px;color:#fff;font-weight:700;font-size:23px;display:flex;align-items:center;gap:10px}
  .contact svg{width:26px;height:22px}
  .contact-email{top:1004px}
  .contact-phone{top:1040px}
  .address{position:absolute;left:540px;top:1026px;display:flex;align-items:center;gap:10px;color:#fff;font-weight:700;font-size:20px;line-height:22px}
  .address svg{width:28px;height:28px}
  .address-lines{border-left:2px solid #fff;padding-left:8px}
</style>
</head>
<body>
<main class="flyer">
  <svg class="flyer-shapes" viewBox="0 0 770 1090" width="770" height="1090" aria-hidden="true">
    <defs>
      <linearGradient id="bandGreen" x1="0" y1="0" x2="1" y2="0">
        <stop offset="0" stop-color="#17a52f"/><stop offset=".6" stop-color="#1fc03a"/><stop offset="1" stop-color="#0f8a25"/>
      </linearGradient>
    </defs>
    <polygon points="0,410 770,277 770,284 0,417" fill="#2fa0e0"/>
    <polygon points="0,415 770,284 770,432 0,534" fill="url(#bandGreen)"/>
    <polygon points="0,534 770,432 770,562 0,636" fill="var(--ink)"/>
    <polygon points="0,636 770,562 770,600 0,660" fill="#b9bcbe" opacity=".6"/>
    <polygon points="0,891 770,891 770,971 0,971" fill="var(--kelly-deep)"/>
    <polygon points="0,971 770,971 770,1090 0,1090" fill="var(--kelly-bright)"/>
    <polygon points="770,968 770,1090 320,1090" fill="var(--ink)"/>
  </svg>

  <div class="brand">
    <span class="brand-mark"></span>
    <span class="brand-name">MARKWELL</span>
  </div>

  <div class="cta cta-top">CALL, EMAIL OR STOP</div>
  <div class="cta cta-bottom">IN TODAY!</div>

  <section class="offer">
    <h1 class="offer-headline">We are offering a youth<br>sports special price on<br><span class="hl">3x5 ft</span> team banners for <span class="hl">$115</span></h1>
    <p class="offer-note">The pricing will include 1 layout<br>with up to 2 revisions</p>
  </section>

  <figure class="sample sample-soccer">
    <span class="sample-tag">Samples</span>
    <div class="sample-art" role="img" aria-label="Sample soccer team banner in blue with mascot artwork and player roster"></div>
  </figure>
  <figure class="sample sample-baseball">
    <span class="sample-tag">Samples</span>
    <div class="sample-art" role="img" aria-label="Sample baseball team banner in black and orange with panther artwork and player roster"></div>
  </figure>

  <p class="turnaround">we will be producing the banners withing 1-2 business days after artwork approval and we would like the potential customer to email us their teams name, roster, and colors to help speed up the layout process.</p>

  <div class="contact contact-email">
    <svg viewBox="0 0 26 22" aria-hidden="true"><rect x="2" y="3" width="22" height="16" fill="none" stroke="#fff" stroke-width="2"/><polyline points="2,3 13,12 24,3" fill="none" stroke="#fff" stroke-width="2"/></svg>
    <span>email: info@markwell202.example</span>
  </div>
  <div class="contact contact-phone">
    <svg viewBox="0 0 26 22" aria-hidden="true"><path d="M3 7 Q13 1 23 7 L20 10 L17 8 L9 8 L6 10 Z" fill="none" stroke="#fff" stroke-width="2"/><rect x="6" y="12" width="14" height="8" rx="1" fill="none" stroke="#fff" stroke-width="2"/></svg>
    <span>phone: 805-219-6847</span>
  </div>

  <div class="address">
    <svg viewBox="0 0 28 28" aria-hidden="true"><polyline points="2,14 14,3 26,14" fill="none" stroke="#fff" stroke-width="2.5"/><path d="M6 12 V25 H22 V12" fill="none" stroke="#fff" stroke-width="2.5"/><rect x="12" y="17" width="5" height="8" fill="#fff"/></svg>
    <div class="address-lines">4816 Corliss<br>Ln. Paso Robles</div>
  </div>
</main>
</body>
</html>
```